We need a banner ad design for a company based in Brazil called "Zunaro" (http://www.zunaro-exemplo.com.br), which offers escort services for men. Our main strength and focus is helping people easily search for escorts using mobile devices, by being an mobile optimized repository of escorts which are crawled from many non-mobile optimized sites.

Target Market(s)

Men at all ages (above 18) looking for escorts

Industry/Entity Type

Escort

Requirements
Must have
• Size must be 468x60
The logo must be on white background
Nice to have
• The banner could have an eye-catching animation

The banner could have a small and quick animation showing the usage of the mobile application (like navigating through the application).
Should not have
• If animated then the text should not be split between frames.

```html
<!DOCTYPE html>
<html lang="pt-BR">
<head>
<meta charset="utf-8">
<title>Zunaro – banner</title>
<link rel="stylesheet" href="https://fonts.googleapis.com/css2?family=Cabin:wght@600;700&display=swap">
<style>
  :root {
    --stage-dark: #1b1b1b;
    --stage-stripe: #232323;
    --ink: #2f2f2f;
    --brand-red: #b3121c;
    --deep-red: #6e0a10;
    --paper: #ffffff;
    --caption: #ececec;
  }
  * { margin: 0; padding: 0; box-sizing: border-box; }
  html, body { width: 1200px; height: 256px; overflow: hidden; }
  body {
    position: relative;
    font-family: "Cabin", "Trebuchet MS", sans-serif;
    background:
      repeating-linear-gradient(135deg, var(--stage-stripe) 0 2px, var(--stage-dark) 2px 5px);
  }
  .banner {
    position: absolute; left: 34px; top: 17px; width: 1132px; height: 72px;
    display: flex; background: var(--deep-red);
    box-shadow: 0 2px 6px rgba(0,0,0,.6);
  }
  .banner__logo {
    width: 136px; background: var(--paper);
    display: flex; align-items: center; justify-content: center; gap: 7px;
  }
  .banner__logo-dot { width: 12px; height: 12px; border-radius: 50%; background: var(--brand-red); }
  .banner__logo-name { font-weight: 700; font-size: 26px; color: var(--brand-red); }
  .banner__band {
    width: 22px;
    background: linear-gradient(90deg, var(--deep-red), var(--brand-red), var(--deep-red));
  }
  .banner__headline {
    width: 751px; background: linear-gradient(180deg, #ffffff, #ececec);
    display: flex; align-items: center; padding-left: 14px;
    font-weight: 700; font-size: 28px; color: var(--ink); white-space: nowrap;
  }
  .banner__headline .accent { color: var(--brand-red); position: relative; margin: 0 6px; }
  .banner__headline .accent svg { position: absolute; left: -4px; bottom: -6px; }
  .banner__band--right { width: 27px; }
  .banner__app-preview {
    flex: 1;
    background: linear-gradient(90deg, #3a3a3a 0 6%, #f4f4f4 6% 85%, #2e2e2e 85%);
  }
  .caption {
    position: absolute; left: 0; width: 1200px; text-align: center;
    font-weight: 700; color: var(--caption);
    text-shadow: 0 2px 3px rgba(0,0,0,.8);
  }
  .caption--link { top: 106px; font-size: 26px; }
  .caption--type { top: 156px; font-size: 26px; }
  .caption--size { top: 192px; font-size: 26px; }
</style>
</head>
<body>
  <div class="banner">
    <div class="banner__logo">
      <span class="banner__logo-dot"></span>
      <span class="banner__logo-name">Zunaro</span>
    </div>
    <div class="banner__band"></div>
    <div class="banner__headline">
      O<span class="accent">maior<svg width="80" height="10" viewBox="0 0 80 10"><path d="M2 7 Q40 1 78 6" stroke="#b3121c" stroke-width="2.5" fill="none"/></svg></span>catálogo de acompanhantes na palma da sua mão.
    </div>
    <div class="banner__band banner__band--right"></div>
    <div class="banner__app-preview" role="img" aria-label="Celular mostrando o perfil de uma acompanhante no aplicativo, com um dedo tocando a tela"></div>
  </div>

  <p class="caption caption--link">Link to animation in the description.</p>
  <p class="caption caption--type">File extension: *.GIF</p>
  <p class="caption caption--size">File size: 296 KB</p>
</body>
</html>
```